Esthetically Pleasing Core Values and Brand Promise for Accounting Firm

I would like a cohesive design that ties together my core values and brand promise. My firm, Maple Finch Advisory, provides accounting work to small businesses. I prefer modern and clean designs. I want my Core Values and Brand Promise to represent me - sole entrepreneur, married, mother of two kids, modern esthetics, clean lines, organized, colorful (teals, greys, white, yellows)

Industry/Entity Type

Public Accounting

Colors
33b8a4

```html
<!DOCTYPE html>
<html lang="en">
<head>
<meta charset="utf-8">
<title>Maple Finch Advisory – Core Values and Brand Promise</title>
<link href="https://fonts.googleapis.com/css2?family=Poppins:wght@300;400;500;600;700;800&display=swap" rel="stylesheet">
<style>
  :root{
    --teal:#33b8a4;
    --teal-deep:#1f9a86;
    --grey:#6b6b6b;
    --ink:#2b2b2b;
    --paper:#f4f4f4;
    --card:#e9e9e9;
    --white:#ffffff;
    --text:#333333;
  }
  *{margin:0;padding:0;box-sizing:border-box}
  html,body{width:892px;height:1200px;overflow:hidden;background:var(--paper)}
  body{font-family:"Poppins",sans-serif;color:var(--text);position:relative}
  .hero{position:absolute;left:0;top:0;width:892px;height:232px;
    background:radial-gradient(ellipse at 70% 30%,#5fe0c8 0%,transparent 55%),
      linear-gradient(100deg,#0f4f55 0%,#1f8a83 35%,#2aa896 60%,#13605f 100%)}
  .hero-band{position:absolute;left:0;top:232px;width:892px;height:26px;background:var(--teal)}
  .brand-ring{position:absolute;left:331px;top:119px;width:230px;height:230px;border-radius:50%;background:var(--teal)}
  .brand-disc{position:absolute;left:343px;top:129px;width:206px;height:206px;border-radius:50%;background:var(--white);
    display:flex;align-items:center;justify-content:center;text-align:center}
  .brand-name{font-weight:400;color:var(--teal-deep);font-size:26px;line-height:1.15;letter-spacing:1px;text-transform:uppercase}
  .values-title{position:absolute;left:293px;top:364px;width:305px;height:56px}
  .values-title span{position:absolute;left:0;top:0;width:100%;height:46px;display:flex;align-items:center;justify-content:center;
    color:var(--white);font-weight:800;font-size:29px;letter-spacing:.5px}
  .timeline{position:absolute;left:0;top:440px;width:892px;height:2px;background:var(--ink)}
  .marker{position:absolute;top:430px;width:22px;height:22px;border-radius:50%;border:2px solid var(--paper);
    color:var(--white);font-size:12px;font-weight:600;display:flex;align-items:center;justify-content:center}
  .stem{position:absolute;top:450px;width:2px;height:48px}
  .card{position:absolute;top:496px;width:192px;height:240px}
  .card-frame{position:absolute;left:12px;top:14px;width:178px;height:216px;background:var(--white);
    box-shadow:0 3px 8px rgba(0,0,0,.25);padding:5px}
  .card-body{width:100%;height:100%;background:var(--card)}
  .card-tab{position:absolute;left:0;top:0}
  .card-foot{position:absolute;left:25px;top:230px;width:152px;height:8px;clip-path:polygon(0 0,100% 0,95% 100%,5% 100%)}
  .card-icon{position:absolute;left:70px;top:76px;width:56px;height:56px}
  .card-title{position:absolute;left:12px;top:142px;width:178px;text-align:center;font-size:10px;font-weight:500;text-transform:uppercase}
  .card-text{position:absolute;left:20px;top:160px;width:162px;text-align:center;font-size:9px;line-height:1.3;color:#444}
  .divider{position:absolute;left:102px;top:786px;width:688px;border-top:1px dashed #9a9a9a}
  .promise-title{position:absolute;left:0;top:812px;width:892px;text-align:center;font-weight:700;font-size:37px;color:var(--teal);letter-spacing:-.3px}
  .promise-sub{position:absolute;left:0;top:860px;width:892px;text-align:center;font-size:17px;color:var(--ink);text-transform:uppercase}
  .split{position:absolute;left:446px;top:913px;height:215px;border-left:1px dashed #9a9a9a}
  .service{position:absolute;top:920px;width:280px;text-align:center}
  .service-icon{display:block;margin:0 auto;width:96px;height:84px}
  .service-title{margin-top:30px;font-weight:700;font-size:22px;color:var(--teal);text-transform:uppercase;line-height:1.2}
  .service-text{margin-top:2px;font-size:11.5px;line-height:1.25;color:var(--ink);text-align:justify;text-align-last:center}
  .footer{position:absolute;left:0;top:1161px;width:892px;height:39px;background:var(--ink)}
</style>
</head>
<body>
  <div class="hero" role="img" aria-label="Teal photo of financial charts and data screens"></div>
  <div class="hero-band"></div>
  <div class="brand-ring"></div>
  <div class="brand-disc"><div class="brand-name">Maple<br>Finch<br>Advisory</div></div>

  <div class="values-title">
    <svg width="305" height="56" viewBox="0 0 305 56">
      <polygon points="8,12 297,12 305,36 295,56 10,56 0,36" fill="var(--ink)"/>
      <polygon points="12,0 290,0 298,23 290,46 12,46 4,23" fill="var(--teal)"/>
    </svg>
    <span>CORE VALUES</span>
  </div>

  <div class="timeline"></div>
  <div class="marker" style="left:72px;background:var(--teal-deep)">1</div>
  <div class="stem" style="left:82px;background:var(--teal-deep)"></div>
  <div class="marker" style="left:279px;background:var(--teal)">2</div>
  <div class="stem" style="left:289px;background:var(--teal)"></div>
  <div class="marker" style="left:486px;background:var(--grey)">3</div>
  <div class="stem" style="left:496px;background:var(--grey)"></div>
  <div class="marker" style="left:691px;background:var(--ink)">4</div>
  <div class="stem" style="left:701px;background:var(--ink)"></div>

  <!-- value 1 -->
  <div class="card" style="left:42px">
    <div class="card-frame"><div class="card-body"></div></div>
    <svg class="card-tab" width="126" height="70" viewBox="0 0 126 70">
      <polygon points="0,0 84,0 124,60 12,60 12,70 0,60" fill="var(--teal-deep)"/>
      <circle cx="44" cy="30" r="21" fill="none" stroke="var(--white)" stroke-width="3"/>
      <text x="44" y="40" text-anchor="middle" font-family="Poppins,sans-serif" font-size="28" font-weight="500" fill="var(--white)">1</text>
    </svg>
    <div class="card-icon" role="img" aria-label="Raised fist icon" style="border-radius:12px;background:rgba(31,154,134,.18)"></div>
    <div class="card-title" style="color:var(--teal-deep)">Empower</div>
    <div class="card-text">we are dedicated, appreciative and respectful of people's time and purpose.</div>
    <div class="card-foot" style="background:var(--teal-deep)"></div>
  </div>

  <!-- value 2 -->
  <div class="card" style="left:248px">
    <div class="card-frame"><div class="card-body"></div></div>
    <svg class="card-tab" width="126" height="70" viewBox="0 0 126 70">
      <polygon points="0,0 84,0 124,60 12,60 12,70 0,60" fill="var(--teal)"/>
      <circle cx="44" cy="30" r="21" fill="none" stroke="var(--white)" stroke-width="3"/>
      <text x="44" y="40" text-anchor="middle" font-family="Poppins,sans-serif" font-size="28" font-weight="500" fill="var(--white)">2</text>
    </svg>
    <svg class="card-icon" viewBox="0 0 56 56" fill="none" stroke="var(--teal)" stroke-width="2">
      <circle cx="28" cy="28" r="20"/>
      <path d="M28 2v10M28 44v10M2 28h10M44 28h10"/>
      <circle cx="28" cy="23" r="6"/>
      <path d="M17 40c2-7 6-10 11-10s9 3 11 10"/>
    </svg>
    <div class="card-title" style="color:var(--teal)">Client Focused</div>
    <div class="card-text">we provide a personal service that goes above the standards of professional care.</div>
    <div class="card-foot" style="background:var(--teal)"></div>
  </div>

  <!-- value 3 -->
  <div class="card" style="left:454px">
    <div class="card-frame"><div class="card-body"></div></div>
    <svg class="card-tab" width="126" height="70" viewBox="0 0 126 70">
      <polygon points="0,0 84,0 124,60 12,60 12,70 0,60" fill="var(--grey)"/>
      <circle cx="44" cy="30" r="21" fill="none" stroke="var(--white)" stroke-width="3"/>
      <text x="44" y="40" text-anchor="middle" font-family="Poppins,sans-serif" font-size="28" font-weight="500" fill="var(--white)">3</text>
    </svg>
    <svg class="card-icon" viewBox="0 0 56 56" fill="none" stroke="var(--grey)" stroke-width="2.5">
      <path d="M28 8v38M8 12h40M18 50h20"/>
      <path d="M12 12L4 32M12 12l8 20M44 12l-8 20M44 12l8 20"/>
      <path d="M3 32a9 6 0 0 0 18 0zM35 32a9 6 0 0 0 18 0z" fill="var(--grey)"/>
    </svg>
    <div class="card-title" style="color:#555">Rectitude</div>
    <div class="card-text">we know the difference between what we have the right to do and what the right thing to do is.</div>
    <div class="card-foot" style="background:var(--grey)"></div>
  </div>

  <!-- value 4 -->
  <div class="card" style="left:660px">
    <div class="card-frame"><div class="card-body"></div></div>
    <svg class="card-tab" width="126" height="70" viewBox="0 0 126 70">
      <polygon points="0,0 84,0 124,60 12,60 12,70 0,60" fill="var(--ink)"/>
      <circle cx="44" cy="30" r="21" fill="none" stroke="var(--white)" stroke-width="3"/>
      <text x="44" y="40" text-anchor="middle" font-family="Poppins,sans-serif" font-size="28" font-weight="500" fill="var(--white)">4</text>
    </svg>
    <div class="card-icon" role="img" aria-label="Young sprout growing from soil" style="border-radius:12px;background:rgba(43,43,43,.15)"></div>
    <div class="card-title" style="color:var(--ink);font-weight:600">Relentless</div>
    <div class="card-text">we believe that the longer we try to do our best, the better we become.</div>
    <div class="card-foot" style="background:var(--ink)"></div>
  </div>

  <div class="divider"></div>
  <div class="promise-title">BRAND PROMISE</div>
  <div class="promise-sub">Trust, Transparency and Dependability</div>
  <div class="split"></div>

  <section class="service" style="left:167px">
    <svg class="service-icon" viewBox="0 0 96 84" fill="none">
      <path d="M22 1H1v82h21M74 1h21v82H74" stroke="var(--ink)" stroke-width="1.5"/>
      <g stroke="var(--teal)" stroke-width="2">
        <path d="M40 14h16l-5 8M45 22h6M41 22c-10 8-16 20-15 32c1 8 7 10 22 10s21-2 22-10"/>
        <path d="M40 14l5 8"/>
        <path d="M53 34c-2-3-9-3-9 1s9 3 9 8-8 5-10 1M48 30v20"/>
        <path d="M58 60l14-16"/><circle cx="59" cy="47" r="3"/><circle cx="71" cy="58" r="3"/>
      </g>
    </svg>
    <div class="service-title">Tax</div>
    <p class="service-text">Maple Finch Advisory provides all clients with a trusted tax advisor who provides accuracy in all filings and ensures your compliance with all government agencies.</p>
  </section>

  <section class="service" style="left:608px">
    <svg class="service-icon" viewBox="0 0 96 84" fill="none">
      <path d="M22 1H1v82h21M74 1h21v82H74" stroke="var(--ink)" stroke-width="1.5"/>
      <g stroke="var(--teal)" stroke-width="2">
        <path d="M44 14h20l8 8v36H44z"/><path d="M64 14v8h8M50 28h16M50 35h16M50 42h16M50 49h16"/>
        <rect x="22" y="26" width="28" height="44" rx="2" fill="var(--paper)"/>
        <rect x="27" y="31" width="18" height="8"/>
        <path d="M27 45h5v5h-5zM34 45h5v5h-5zM41 45h4v5h-4zM27 53h5v5h-5zM34 53h5v5h-5zM41 53h4v5h-4zM27 61h5v4h-5zM34 61h5v4h-5zM41 61h4v4h-4z"/>
      </g>
    </svg>
    <div class="service-title">Accounting</div>
    <p class="service-text">Maple Finch Advisory provides all business owners with the financial visibility needed to foster growth and facilitate goals.</p>
  </section>

  <div class="footer"></div>
</body>
</html>
```